Past The Hedge landscaping flyer "looking for BIG impact"

We're doing a big marketing push and having 50,000 flyers distributed around exeter, devon.

A5

The flyer is double sided but withe the same image on each side so it doesn't matter how it lands.

Flyer for landscape gardener and maintenance company.

Solo drop leaflets so really needs to pop.

Would like it to be similar to website

4 elements of flyer are:

Design
Past The Hedge Garden Design offers a full-service garden design consultancy to clients seeking an outside space which is both beautiful and functional, any size, any budget.

Create
We provide high quality, bespoke garden construction for homes and businesses throughout Devon and the South West.

Maintain
Services include grass mowing, hedge trimming and cutting, pruning, weeding, pressure cleaning and lawn care, planting and turfing.

Contact details
Office 01392 417258
Mobile 07714623581
Rkellaway@pastthehedgeltd.example
Www.pastthehedgeltd.example

Images and company logo attached.

I've added something I have very crudely mocked up. Use it or ignore it, I really don't mind.

I've added two pics for maintenance, one is a few hand tools and one is a mower. Up to you which one you choose.

Cheers!

Reason: Deadline extended. We aren't so rushed now so we're taking the pressure off. Really impressed with what we've received so far!

Requirements
Must have
• BIG IMPACT.
• EYE CATCHING
• SHOWS WHAT WE DO.
• Maintain brand recognition.

```html
<!DOCTYPE html>
<html lang="en">
<head>
<meta charset="utf-8">
<title>Past The Hedge – Flyer</title>
<link rel="stylesheet" href="https://fonts.googleapis.com/css2?family=Archivo+Black&family=Arimo:wght@400;700&display=swap">
<style>
  :root {
    --page: #ffffff;
    --sky-top: #1f5fb0;
    --sky-mid: #6fa6dc;
    --sky-low: #c9def0;
    --grass-light: #8cc63f;
    --grass-dark: #2f7d1f;
    --lime: #9fcb3e;
    --tab-dark: #263a2a;
    --panel-green: #2f9447;
    --ink: #2d2d2d;
    --white: #ffffff;
  }
  * { box-sizing: border-box; margin: 0; padding: 0; }
  html, body {
    width: 1200px; height: 1000px; overflow: hidden;
    background: var(--page);
    font-family: "Arimo", Arial, sans-serif;
  }
  .flyer {
    position: absolute; left: 12px; top: 86px;
    width: 1176px; height: 828px; overflow: hidden;
  }
  .backdrop {
    position: absolute; inset: 0;
    background: linear-gradient(180deg,
      var(--sky-top) 0%, var(--sky-mid) 30%, var(--sky-low) 50%,
      var(--grass-light) 66%, var(--grass-dark) 100%);
  }
  .brand {
    position: absolute; left: 40px; top: 110px;
    display: flex; align-items: center; gap: 12px;
  }
  .brand-dot {
    width: 34px; height: 34px; border-radius: 50%;
    background: var(--panel-green);
  }
  .brand-name {
    font-family: "Archivo Black", "Arial Black", sans-serif;
    font-size: 30px; color: var(--tab-dark); letter-spacing: 0.5px;
  }
  .tagline {
    position: absolute; right: 20px; top: 62px;
    color: var(--white); font-weight: 700; font-size: 19px; letter-spacing: 0.3px;
  }
  .service {
    position: absolute; width: 340px;
  }
  .service-card {
    border: 7px solid var(--lime); border-radius: 34px;
    background: var(--panel-green); overflow: hidden;
    box-shadow: 0 0 0 2px var(--tab-dark);
  }
  .service-photo { width: 100%; }
  .service-text {
    color: var(--white); font-size: 18.5px; line-height: 1.2;
    text-align: center; padding: 18px 16px 22px;
  }
  .service-text b { font-weight: 700; }
  .service-tab {
    position: absolute; top: -52px;
    height: 76px; padding: 0 26px;
    background: var(--tab-dark); border: 6px solid var(--lime); border-radius: 18px;
    display: flex; align-items: center; justify-content: center;
    font-family: "Archivo Black", "Arial Black", sans-serif;
    font-size: 44px; color: var(--lime); letter-spacing: 1px;
  }
  .service--design { left: 48px; top: 345px; transform: rotate(5deg); }
  .service--design .service-tab { left: 78px; width: 260px; }
  .service--design .service-photo { height: 240px; background: linear-gradient(135deg, #efe9dc, #d9cfc0 60%, #c6a7b6); }

  .service--create { left: 420px; top: 222px; transform: rotate(-6deg); }
  .service--create .service-tab { left: 18px; width: 250px; }
  .service--create .service-photo { height: 250px; background: linear-gradient(180deg, #e8e4dc 0%, #c9b79b 45%, #b5b0a6 70%, #5f8d3a 100%); }

  .service--maintain { left: 782px; top: 160px; transform: rotate(5deg); }
  .service--maintain .service-tab { left: 60px; width: 270px; }
  .service--maintain .service-photo { height: 230px; background: linear-gradient(160deg, #5c8f2e, #3f7a22 60%, #c9452b); }

  .contact {
    position: absolute; right: 0; bottom: 0;
    width: 368px; height: 144px;
    background: var(--lime); border-top-left-radius: 40px;
    text-align: right; padding: 14px 20px 0 0;
    color: var(--ink); font-size: 17.5px; line-height: 1.3;
  }
  .contact-web { font-weight: 700; font-size: 21px; margin-top: 4px; }
</style>
</head>
<body>
<main class="flyer">
  <div class="backdrop" role="img" aria-label="Blue sky with clouds above long green grass"></div>

  <div class="brand">
    <span class="brand-dot"></span>
    <span class="brand-name">PAST THE HEDGE</span>
  </div>

  <p class="tagline">LANDSCAPE GARDENER &amp; MAINTENANCE COMPANY.</p>

  <section class="service service--design">
    <div class="service-card">
      <div class="service-photo" role="img" aria-label="Hand-coloured garden design plan with planting circles"></div>
      <p class="service-text">Past The Hedge Garden Design offers a <b>full-service garden design consultancy</b> to clients seeking an outside space which is both <b>beautiful and functional, any size, any budget.</b></p>
    </div>
    <h2 class="service-tab">DESIGN</h2>
  </section>

  <section class="service service--create">
    <div class="service-card">
      <div class="service-photo" role="img" aria-label="New timber planter along a paved path between two house doors"></div>
      <p class="service-text">We provide <b>high quality, bespoke garden construction</b> for homes and businesses throughout <b>Devon and the South West.</b></p>
    </div>
    <h2 class="service-tab">CREATE</h2>
  </section>

  <section class="service service--maintain">
    <div class="service-card">
      <div class="service-photo" role="img" aria-label="Power garden tools laid out on a lawn"></div>
      <p class="service-text"><b>Services include</b><br>grass mowing,<br>hedge trimming and cutting,<br>pruning, weeding,<br>pressure cleaning and<br>lawn care,<br>planting and turfing.</p>
    </div>
    <h2 class="service-tab">MAINTAIN</h2>
  </section>

  <address class="contact" style="font-style:normal">
    <div>Office: 01392 417258</div>
    <div>Mobile: 07714623581</div>
    <div>Rkellaway@pastthehedgeltd.example</div>
    <div class="contact-web">www.pastthehedgeltd.example</div>
  </address>
</main>
</body>
</html>
```